Hypnotherapy- past life regression-life between lives therapist needs a website

I need a website that is enticing and spiritual in its feeling. It needs to have a lot of beautiful nature pictures included. The theme is "Quiet Harbor Path- what might you find....Lessons Solutions Answers"
Because all of us have the answers to living our best life, they are in our subconcious. But not everyone is capable of accessing them. Hypnosis accesses the subconcious and helps to create new neural pathways in the brain which can create new behaviors and responses to situations.
Hypnosis can help with anxiety, pain relief, weight loss, smoking/vaping cessation, self confidence......anything about yourself that you want to change.
Exploration of past lives and life between lives can reveal things related to ones current life. For example, perhaps your fear of deep water is a result of drowning in a past life. Once this has been discovered, it can lead to changes in ones current life.
Almost any personal behavior one wants to change, can be helped through hypnotherapy.
I need a page for testimonials, a place for scheduling (I will have a link to my scheduling app) some information about hypnotherapy.
I am uploading my logo files. My business card will be using the black and gold style, but my website does not have to reflect that. It can be based on the caramel and deep green like full color logo. Earthy, calm colors.
I also like the mock up of my logo on the beach and there was one on a starry night sky that I also liked.
Target Market(s)
men and women ages 25-50
Industry/Entity Type
natural health and wellness, spirituality
Number of Pages Required
4 page
Requirements
Must have
- a page for testimonials, perhaps with a beautiful nature picture with each one, I will have approximately 6. A link to schedule a complimentary intro session, preferably on the first page
Should not have
- no swinging watches or other sterotyped hypnosis symbols

```html
<!DOCTYPE html>
<html lang="en">
<head>
<meta charset="utf-8">
<title>Quiet Harbor Path – Hypnotherapy</title>
<link rel="stylesheet" href="https://fonts.googleapis.com/css2?family=Young+Serif&family=Mulish:wght@400;600;700&family=DM+Sans:wght@400;500;700&display=swap">
<style>
:root{
  --olive:#4f5628;
  --olive-dark:#3f4520;
  --caramel:#e0852b;
  --caramel-soft:#e89a4c;
  --cream:#fdf2e2;
  --ink:#2b2b2b;
  --muted:#6d6d6d;
  --link:#2f6fd6;
  --white:#ffffff;
}
*{box-sizing:border-box;margin:0;padding:0}
html,body{width:1200px;height:4814px;overflow:hidden}
body{position:relative;background:var(--white);font-family:"Mulish",sans-serif;color:var(--ink)}
.abs{position:absolute}
.serif{font-family:"Young Serif",serif}
.btn{position:absolute;display:flex;align-items:center;justify-content:center;border-radius:30px;color:var(--white);font-family:"Mulish",sans-serif;font-weight:600;font-size:13px;letter-spacing:.3px;text-transform:uppercase}
.btn-olive{background:var(--olive)}
.btn-caramel{background:var(--caramel)}

/* header */
.brand{position:absolute;left:96px;top:60px;display:flex;align-items:center;gap:10px}
.brand-dot{width:22px;height:22px;border-radius:50%;background:var(--caramel)}
.brand-name{font-family:"Young Serif",serif;font-size:17px;color:var(--caramel)}
.main-nav{position:absolute;top:66px;left:397px;display:flex;gap:0}
.main-nav a{font-size:13.5px;color:var(--ink);text-decoration:none;margin-right:22px}

/* hero */
.hero-photo{position:absolute;left:0;top:150px;width:1200px;height:730px;
  background:linear-gradient(180deg,rgba(255,255,255,1) 0%,#f7ead6 18%,#f4cf96 36%,#e9b775 42%,#7ea6a3 52%,#5f8d8c 60%,#d9b38c 72%,#f0c79a 82%,#fbe7d4 92%,#fff 100%)}
.hero-title{position:absolute;top:208px;width:1200px;text-align:center;font-size:70px;color:var(--olive);letter-spacing:1px}
.hero-sub{position:absolute;top:292px;width:1200px;text-align:center;font-size:19px;line-height:24px;color:var(--ink)}

/* about */
.about-photo{position:absolute;border-radius:18px;overflow:hidden}
.about-photo.back{left:271px;top:953px;width:327px;height:355px;border:6px solid var(--olive);background:linear-gradient(135deg,#c9d6df,#e8e2d4 55%,#b9c3b0)}
.about-photo.front{left:136px;top:1069px;width:271px;height:277px;border:6px solid var(--caramel);background:linear-gradient(135deg,#5d8a2f,#7fae47 50%,#a7c4d6);box-shadow:0 14px 30px rgba(0,0,0,.18)}
.about-title{position:absolute;left:650px;top:1000px;font-size:30px;color:var(--olive)}
.about-text{position:absolute;left:650px;top:1056px;width:390px;font-size:12.5px;line-height:16px}
.about-text p{margin-bottom:13px}

/* solutions */
.solutions-bg{position:absolute;left:0;top:1440px;width:1200px;height:780px}
.solutions-title{position:absolute;top:1524px;width:1200px;text-align:center;font-size:29px;color:var(--white)}
.solutions-text{position:absolute;top:1594px;left:240px;width:720px;text-align:center;color:var(--white);font-size:14px;line-height:19px}
.solutions-text p{margin-bottom:19px}
.service{position:absolute;top:1804px;width:231px;height:205px;background:var(--white)}
.service-photo{height:153px}
.service-name{height:52px;display:flex;align-items:center;justify-content:center;font-family:"Young Serif",serif;font-size:17px;color:var(--ink)}

/* testimonials */
.section-title{position:absolute;width:1200px;text-align:center;font-size:29px;color:var(--olive)}
.review{position:absolute;background:var(--white);box-shadow:0 4px 18px rgba(0,0,0,.12);border-radius:4px;text-align:center}
.review-head{display:flex;align-items:center;text-align:left}
.avatar{border-radius:50%;background:linear-gradient(135deg,#a79b8c,#6f6358)}
.stars{color:var(--caramel);letter-spacing:1px}
.review.side{top:2374px;width:233px;height:254px;padding:28px 16px}
.review.side .avatar{width:48px;height:48px;margin-right:10px}
.review.side .name{font-size:13px;font-weight:700}
.review.side .role{font-size:9px}
.review.side .stars{font-size:11px;margin-left:8px}
.review.side h4{font-size:13.5px;margin:18px 0 8px;font-weight:600}
.review.side p{font-size:9px;line-height:11.5px}
.review.main{left:443px;top:2310px;width:331px;height:350px;padding:28px 20px}
.review.main .avatar{width:58px;height:58px;margin-right:12px}
.review.main .name{font-size:17px;font-weight:700}
.review.main .role{font-size:13px}
.review.main .stars{font-size:17px;margin-left:18px}
.review.main h4{font-size:17px;margin:22px 0 16px;font-weight:600}
.review.main p{font-size:13.5px;line-height:18px}
.pager{position:absolute;top:2694px;left:480px;width:260px;display:flex;align-items:center;justify-content:space-between}
.dot{width:13px;height:13px;border-radius:50%;background:#cfcfcf}
.dot.on{background:#7c7c7c}

/* blog */
.mountains{position:absolute;left:0;top:2830px;width:1200px;height:770px;background:linear-gradient(180deg,#fff 0%,#dfe3df 10%,#a8b2aa 26%,#7e8d82 45%,#6d7f72 62%,#c7d0c9 85%,#fff 100%)}
.post{position:absolute;top:3050px;width:307px;height:469px;background:var(--white);box-shadow:0 4px 16px rgba(0,0,0,.1);font-family:"DM Sans",sans-serif}
.post-photo{height:221px}
.post-body{padding:30px 26px}
.post-meta{font-size:10.5px;color:var(--muted)}
.post h3{font-size:16px;font-weight:500;color:var(--olive-dark);line-height:21px;margin:10px 0 12px}
.post p{font-size:11.5px;line-height:17px;color:var(--muted)}
.post-link{display:inline-flex;align-items:center;gap:8px;margin-top:26px;border:1px solid #c9d3e6;padding:9px 18px;font-size:10px;font-weight:700;color:var(--link)}

/* contact */
.learn{position:absolute;left:117px;top:3708px;width:340px;font-family:"DM Sans",sans-serif}
.learn h2{font-size:28px;line-height:33px;font-weight:500;color:#222}
.learn p{font-size:12.5px;line-height:20px;margin-top:26px;color:#333}
.contact-item{position:absolute;left:117px;display:flex;align-items:center;gap:14px;font-family:"DM Sans",sans-serif;font-size:11px;line-height:14px}
.contact-icon{width:52px;height:52px;border-radius:50%;background:var(--caramel);display:flex;align-items:center;justify-content:center}
.contact-panel{position:absolute;left:505px;top:3691px;width:648px;height:537px;background:var(--cream);border-radius:34px;font-family:"DM Sans",sans-serif}
.contact-panel h2{position:absolute;left:42px;top:80px;font-size:27px;font-weight:500;color:#222}
.field{position:absolute;border:1.5px solid var(--olive);font-size:13px;padding:14px 20px;color:#333;background:transparent}
.submit{position:absolute;left:42px;top:445px;width:160px;height:46px;border-radius:24px;background:var(--olive);color:var(--white);display:flex;align-items:center;justify-content:center;font-size:13px;font-weight:500}

/* footer */
.footer-bg{position:absolute;left:0;top:4270px;width:1200px;height:544px;background:linear-gradient(180deg,#fff 0%,#c9d3d3 16%,#7d9296 38%,#4b6470 60%,#3b5563 80%,#324b5a 100%)}
.footer-brand{position:absolute;top:4560px;width:1200px;display:flex;justify-content:center;align-items:center;gap:12px}
.footer-brand .brand-dot{background:var(--white)}
.footer-brand .brand-name{color:var(--white);font-size:28px}
.footer-nav{position:absolute;top:4696px;width:1200px;display:flex;justify-content:center;gap:34px}
.footer-nav a{color:var(--white);font-size:16px;text-decoration:none}
</style>
</head>
<body>

<!-- header -->
<div class="hero-photo" role="img" aria-label="Sunset over calm ocean waves breaking on a sandy beach"></div>
<header>
  <div class="brand"><span class="brand-dot"></span><span class="brand-name">Quiet Harbor Path</span></div>
  <nav class="main-nav">
    <a>Home</a><a>Hypnosis Solutions</a><a>About Us</a><a>Testimonials</a><a>Blog</a><a>Contact</a>
  </nav>
  <div class="btn btn-caramel" style="left:914px;top:60px;width:174px;height:36px">Make Appointment</div>
</header>

<section class="hero">
  <h1 class="hero-title serif">Don't Suffer in silence</h1>
  <p class="hero-sub">Let Hypnotherapy help you get to the root of your issues and make<br>positive changes to your life</p>
  <div class="btn btn-olive" style="left:514px;top:362px;width:172px;height:34px">Make Appointment</div>
</section>

<!-- about -->
<section class="about">
  <div class="about-photo back" role="img" aria-label="Woman sitting peacefully with eyes closed in soft daylight"></div>
  <div class="about-photo front" role="img" aria-label="Man relaxing on green grass, smiling"></div>
  <svg class="abs" style="left:1044px;top:946px" width="40" height="40" viewBox="0 0 24 24"><path fill="#e0852b" d="M12 1l2.9 7.6H23l-6.5 4.9 2.5 8L12 16.8 5 21.5l2.5-8L1 8.6h8.1z"/></svg>
  <svg class="abs" style="left:120px;top:1270px" width="30" height="30" viewBox="0 0 24 24"><path fill="#e0852b" d="M12 1l2.9 7.6H23l-6.5 4.9 2.5 8L12 16.8 5 21.5l2.5-8L1 8.6h8.1z"/></svg>
  <h2 class="about-title serif">Who We Are</h2>
  <div class="about-text">
    <p>Lorem ipsum dolor sit amet consectetur. Volutpat turpis quam euismod ac est. Lacinia ac cursus sodales donec aliquam accumsan. A blandit vitae nunc aliquet tempor platea lectus. Pretium aliquam auctor nisl bibendum pretium imperdiet. Sed tristique et auctor nisl enim. Nisl adipiscing vulputate volutpat facilisi dignissim tristique lectus.</p>
    <p>Nisl amet tellus eget etiam eget. Justo non diam cursus lobortis condimentum. Malesuada at.</p>
  </div>
  <div class="btn btn-caramel" style="left:657px;top:1229px;width:172px;height:34px">Read More</div>
</section>

<!-- solutions -->
<section class="solutions">
  <svg class="solutions-bg" viewBox="0 0 1200 780" preserveAspectRatio="none">
    <defs>
      <linearGradient id="bandFade" x1="0" y1="0" x2="0" y2="1">
        <stop offset="0" stop-color="#e0852b"/>
        <stop offset="0.74" stop-color="#e0852b"/>
        <stop offset="0.86" stop-color="#f3c79b"/>
        <stop offset="1" stop-color="#ffffff"/>
      </linearGradient>
    </defs>
    <path d="M0 58 C 300 0 800 -10 1200 66 L1200 780 L0 780 Z" fill="url(#bandFade)"/>
  </svg>
  <h2 class="solutions-title serif">Hypnotherapy Solutions</h2>
  <div class="solutions-text">
    <p>There is a time in all our lives when we need a bit of a helping hand, whether it's a shoulder to lean on, or some inspiration to make changes.</p>
    <p>Hypnosis can help you to find what you are looking for. We work together as a team; hypnotist and client, to find the most effective route to resolution.</p>
    <p>If you're looking for hypnotherapy in London then we could be your perfect solution. Today you could take the first step to a new you.</p>
  </div>
  <div class="service" style="left:114px"><div class="service-photo" role="img" aria-label="Hands breaking a cigarette" style="background:linear-gradient(135deg,#6b6f74,#c9b3a2 55%,#55595d)"></div><div class="service-name">Addiction</div></div>
  <div class="service" style="left:361px"><div class="service-photo" role="img" aria-label="Person sitting alone in a dim room" style="background:linear-gradient(135deg,#2f3438,#5c6266 50%,#3a3f43)"></div><div class="service-name">Anxiety</div></div>
  <div class="service" style="left:609px"><div class="service-photo" role="img" aria-label="Abstract head dissolving into colorful particles" style="background:radial-gradient(circle at 55% 45%,#d2663a,#6b3d4c 45%,#1d2a33 85%)"></div><div class="service-name">Overcoming Trauma</div></div>
  <div class="service" style="left:856px"><div class="service-photo" role="img" aria-label="Magnifying glass over medical blocks" style="background:linear-gradient(135deg,#f4d9d2,#f7e7e1 50%,#e9c3b8)"></div><div class="service-name">Health</div></div>
  <div class="btn btn-olive" style="left:469px;top:2044px;width:262px;height:34px">Book Your Free Consultation</div>
</section>

<!-- testimonials -->
<section class="testimonials">
  <h2 class="section-title serif" style="top:2230px">Testimonials</h2>
  <article class="review side" style="left:161px">
    <div class="review-head"><div class="avatar" role="img" aria-label="Portrait of Leo"></div><div><div class="name">Leo</div><div class="role">Lead Designer</div></div><div class="stars">★★★★☆</div></div>
    <h4>It was a very good experience</h4>
    <p>Lorem ipsum dolor sit amet, consectetur adipiscing elit. Cursus nibh mauris, nec turpis orci lectus maecenas. Suspendisse sed magna eget nibh in turpis. Consequat duis diam lacus arcu. Faucibus venenatis felis id augue sit cursus pellentesque enim arcu. Elementum felis magna pretium in tincidunt. Suspendisse sed magna eget nibh in turpis. Consequat duis diam lacus arcu.</p>
  </article>
  <article class="review main">
    <div class="review-head"><div class="avatar" role="img" aria-label="Portrait of Leo"></div><div><div class="name">Leo</div><div class="role">Ellis Varden, NY</div></div><div class="stars">★★★★★</div></div>
    <h4>It was a very good experience</h4>
    <p>Lorem ipsum dolor sit amet, consectetur adipiscing elit. Cursus nibh mauris, nec turpis orci lectus maecenas. Suspendisse sed magna eget nibh in turpis. Consequat duis diam lacus arcu. Faucibus venenatis felis id augue sit cursus pellentesque enim arcu. Elementum felis magna pretium in tincidunt. Suspendisse sed magna eget nibh in turpis. Consequat duis diam lacus arcu.</p>
  </article>
  <article class="review side" style="left:824px">
    <div class="review-head"><div class="avatar" role="img" aria-label="Portrait of Sarah"></div><div><div class="name">Sarah</div><div class="role">Lead Designer</div></div><div class="stars">★★★★☆</div></div>
    <h4>It was a very good experience</h4>
    <p>Lorem ipsum dolor sit amet, consectetur adipiscing elit. Cursus nibh mauris, nec turpis orci lectus maecenas. Suspendisse sed magna eget nibh in turpis. Consequat duis diam lacus arcu. Faucibus venenatis felis id augue sit cursus pellentesque enim arcu. Elementum felis magna pretium in tincidunt. Suspendisse sed magna eget nibh in turpis. Consequat duis diam lacus arcu.</p>
  </article>
  <div class="pager">
    <svg width="16" height="22" viewBox="0 0 16 22"><path d="M12 3L4 11l8 8" fill="none" stroke="#333" stroke-width="3"/></svg>
    <span class="dot on"></span><span class="dot"></span><span class="dot"></span><span class="dot"></span><span class="dot"></span><span class="dot"></span>
    <svg width="16" height="22" viewBox="0 0 16 22"><path d="M4 3l8 8-8 8" fill="none" stroke="#333" stroke-width="3"/></svg>
  </div>
  <div class="btn btn-olive" style="left:475px;top:2781px;width:262px;height:34px">More Testimonials</div>
</section>

<!-- blog -->
<section class="blog">
  <div class="mountains" role="img" aria-label="Misty green mountain ranges"></div>
  <article class="post" style="left:114px">
    <div class="post-photo" role="img" aria-label="Swirling orange and dark abstract smoke" style="background:radial-gradient(circle at 50% 55%,#e38a3c,#7a4a3a 40%,#1f1d22 80%)"></div>
    <div class="post-body">
      <div class="post-meta">22 Oct, 2020 &nbsp;/&nbsp; 246 Comments</div>
      <h3>Duis magna risus, convallis vel purus eu, sollicitudin volutpat velit.</h3>
      <p>Maecenas blandit auctor tempor. Class aptent taciti sociosqu ad litora torquent per conubia nostra.</p>
      <span class="post-link">READ MORE <svg width="16" height="10" viewBox="0 0 16 10"><path d="M0 5h14M10 1l4 4-4 4" fill="none" stroke="#2f6fd6" stroke-width="1.6"/></svg></span>
    </div>
  </article>
  <article class="post" style="left:447px">
    <div class="post-photo" role="img" aria-label="Woman sitting on a beach facing the calm sea" style="background:linear-gradient(180deg,#b9d4e4,#8fb4c8 55%,#d9c5a6)"></div>
    <div class="post-body">
      <div class="post-meta">8 Sep, 2020 &nbsp;/&nbsp; 246 Comments</div>
      <h3>Donec ut ex eu libero euismod dapibus id quis ipsum.</h3>
      <p>Phasellus non feugiat turpis, non gravida lorem. Nulla fermentum odio in dolor dapibus, ac eleifend lectus ullamcorper.</p>
      <span class="post-link">READ MORE <svg width="16" height="10" viewBox="0 0 16 10"><path d="M0 5h14M10 1l4 4-4 4" fill="none" stroke="#2f6fd6" stroke-width="1.6"/></svg></span>
    </div>
  </article>
  <article class="post" style="left:779px">
    <div class="post-photo" role="img" aria-label="Lifeguard hut on a quiet beach at dusk" style="background:linear-gradient(180deg,#c9b6b0,#b8a39c 45%,#8d7f7c)"></div>
    <div class="post-body">
      <div class="post-meta">24 May, 2020 &nbsp;/&nbsp; 246 Comments</div>
      <h3>Maecenas congue cursus metus eget bibendum phasellus dign.</h3>
      <p>Praesent semper enim at lacus sagittis, non semper eros ullamcorper. Duis id elemtum nisl, eu tincidunt nisl.</p>
      <span class="post-link">READ MORE <svg width="16" height="10" viewBox="0 0 16 10"><path d="M0 5h14M10 1l4 4-4 4" fill="none" stroke="#2f6fd6" stroke-width="1.6"/></svg></span>
    </div>
  </article>
</section>

<!-- contact -->
<section class="contact">
  <div class="learn">
    <h2>Learn More About This Innovative New Treatment Option</h2>
    <p>Lorem ipsum dolor sit amet consectetur. Odio elementum lectus mattis ac nunc sed. Pharetra risus neque proin enim duis felis cras sit tortor. Est commodo sed sed fusce. Vulputate nunc commodo auctor amet neque quisque pretium sed nulla. Ligula sit elit justo rutrum tincidunt.</p>
  </div>
  <div class="contact-item" style="top:3983px">
    <span class="contact-icon"><svg width="22" height="16" viewBox="0 0 22 16"><rect x="1" y="1" width="20" height="14" rx="2" fill="none" stroke="#fff" stroke-width="1.6"/><path d="M1 2l10 7 10-7" fill="none" stroke="#fff" stroke-width="1.6"/></svg></span>
    <span>Email<br>hello@quietharborpath.com</span>
  </div>
  <div class="contact-item" style="top:4061px">
    <span class="contact-icon"><svg width="22" height="22" viewBox="0 0 24 24"><path d="M6.6 10.8a15 15 0 006.6 6.6l2.2-2.2a1 1 0 011-.25 11.4 11.4 0 003.6.6 1 1 0 011 1V20a1 1 0 01-1 1A17 17 0 013 4a1 1 0 011-1h3.5a1 1 0 011 1 11.4 11.4 0 00.6 3.6 1 1 0 01-.25 1z" fill="none" stroke="#fff" stroke-width="1.6"/></svg></span>
    <span>Call Us<br>(00) 555 014 270</span>
  </div>
  <div class="contact-item" style="top:4136px">
    <span class="contact-icon"><svg width="22" height="22" viewBox="0 0 24 24"><circle cx="12" cy="12" r="10" fill="none" stroke="#fff" stroke-width="1.6"/><path d="M12 6v6l4 2" fill="none" stroke="#fff" stroke-width="1.6"/></svg></span>
    <span>Mon – Sat 9.00 – 18.00<br>Sunday Closed</span>
  </div>
  <form class="contact-panel">
    <h2>Get in Touch</h2>
    <div class="field" style="left:42px;top:141px;width:265px;height:48px">First name*</div>
    <div class="field" style="left:339px;top:141px;width:265px;height:48px">Last name*</div>
    <div class="field" style="left:42px;top:217px;width:272px;height:48px">Phone Number*</div>
    <div class="field" style="left:339px;top:217px;width:281px;height:48px">Email*</div>
    <div class="field" style="left:42px;top:293px;width:578px;height:128px">Your Message</div>
    <div class="submit">Submit Message</div>
  </form>
</section>

<!-- footer -->
<footer>
  <div class="footer-bg" role="img" aria-label="Blue misty mountain landscape at dusk"></div>
  <div class="footer-brand"><span class="brand-dot"></span><span class="brand-name">Quiet Harbor Path</span></div>
  <nav class="footer-nav"><a>Home</a><a>Hypnosis Solutions</a><a>About Us</a><a>Testimonials</a><a>Blog</a><a>Contact</a></nav>
</footer>

</body>
</html>
```